business card design for a plumbing contractor

i need a double business card for a plumbing business, our initial service is residential Sewer Drain Cleaning.

Target Market(s)

other plumbing Business

Industry/Entity Type

Plumbing

Contact Information for Business Card

www.PipeworksTopNotch.example- 5173829046-

Font styles to use
Serif

Colors
ec1f27
0455a3

```html
<!DOCTYPE html>
<html lang="en">
<head>
<meta charset="utf-8">
<title>Pipeworks Top Notch – Business Card</title>
<link href="https://fonts.googleapis.com/css2?family=Tinos:wght@400;700&display=swap" rel="stylesheet">
<style>
  :root {
    --brand-red: #ec1f27;
    --brand-blue: #0455a3;
    --brand-grey: #7a7468;
    --ink: #1e1e1e;
    --card: #ffffff;
    --backdrop: #2a2a2a;
  }
  * { box-sizing: border-box; margin: 0; padding: 0; }
  html, body {
    width: 1200px; height: 852px; overflow: hidden;
    background: var(--backdrop);
    font-family: "Tinos", "Times New Roman", serif;
  }
  .canvas {
    position: relative; width: 1200px; height: 852px;
  }
  .card {
    position: absolute;
    width: 700px; height: 400px;
    background: var(--card);
    border-radius: 24px;
    overflow: hidden;
  }
  .card--front { left: 70px; top: 16px; }
  .card--back { left: 430px; top: 436px; }

  .company-name {
    font-weight: 700;
    color: var(--brand-grey);
    line-height: 1.0;
    display: flex; align-items: center; gap: 14px;
  }
  .company-name .mark {
    width: 22px; height: 22px; background: var(--brand-red); flex: none;
  }
  .card--front .company-name {
    position: absolute; left: 60px; top: 110px; font-size: 50px;
  }
  .service-list {
    position: absolute; left: 60px; top: 250px; list-style: none;
    font-size: 24px; color: var(--ink);
  }
  .service-list li {
    display: flex; align-items: center; gap: 14px; margin-bottom: 12px;
  }
  .service-list li::before {
    content: ""; width: 14px; height: 14px; background: var(--brand-red); flex: none;
  }

  .card--back .company-name {
    position: absolute; right: 50px; top: 50px; font-size: 40px;
  }
  .person {
    position: absolute; left: 60px; top: 150px;
  }
  .person-name {
    font-size: 32px; letter-spacing: 1px; text-transform: uppercase; color: var(--brand-grey);
  }
  .person-name .first { color: var(--brand-red); }
  .person-role {
    font-size: 18px; letter-spacing: 1px; text-transform: uppercase; color: var(--brand-blue);
  }
  .contact-list {
    position: absolute; left: 60px; top: 270px; list-style: none;
    font-size: 20px; color: var(--ink);
  }
  .contact-list li {
    display: flex; align-items: center; gap: 14px; margin-bottom: 10px;
  }
  .contact-icon {
    width: 26px; height: 26px; border-radius: 50%;
    background: var(--brand-red); flex: none;
    display: flex; align-items: center; justify-content: center;
  }
</style>
</head>
<body>
<div class="canvas">
  <section class="card card--front">
    <h1 class="company-name"><span class="mark"></span>Pipeworks Top Notch</h1>
    <ul class="service-list">
      <li>Sewer Drain Cleaning</li>
      <li>Maintenance</li>
      <li>Trenchless Pipe Installs.</li>
    </ul>
  </section>

  <section class="card card--back">
    <h2 class="company-name"><span class="mark"></span>Pipeworks Top Notch</h2>
    <div class="person">
      <p class="person-name"><span class="first">Daniel</span> Marlow</p>
      <p class="person-role">Managing Director</p>
    </div>
    <ul class="contact-list">
      <li>
        <span class="contact-icon">
          <svg width="14" height="14" viewBox="0 0 24 24"><path fill="#fff" d="M6.6 10.8a15 15 0 0 0 6.6 6.6l2.2-2.2a1 1 0 0 1 1-.25 11.4 11.4 0 0 0 3.6.6 1 1 0 0 1 1 1V20a1 1 0 0 1-1 1A17 17 0 0 1 3 4a1 1 0 0 1 1-1h3.5a1 1 0 0 1 1 1c0 1.25.2 2.45.6 3.6a1 1 0 0 1-.25 1z"/></svg>
        </span>
        5173829046
      </li>
      <li>
        <span class="contact-icon">
          <svg width="14" height="14" viewBox="0 0 24 24"><rect x="3" y="6" width="18" height="12" fill="none" stroke="#fff" stroke-width="2"/><path d="M3 6l9 7 9-7" fill="none" stroke="#fff" stroke-width="2"/></svg>
        </span>
        Dispatcher@PipeworksTopNotch.example
      </li>
      <li>
        <span class="contact-icon">
          <svg width="14" height="14" viewBox="0 0 24 24"><circle cx="12" cy="12" r="9" fill="none" stroke="#fff" stroke-width="2"/><path d="M3 12h18M12 3c3 3 3 15 0 18M12 3c-3 3-3 15 0 18" fill="none" stroke="#fff" stroke-width="1.6"/></svg>
        </span>
        www.PipeworksTopNotch.example
      </li>
    </ul>
  </section>
</div>
</body>
</html>
```